We need a completed book cover (front and back) for a Christian devotional book titled "Walking Steady Onward: Shaped as an Open PATH Follower" by Dr. Martin Hale. The publishing company should be "Open Path" (https://opnpathhub.org). This will be for small groups to go through together daily to understand how to grow as a Christian as a part of the family of God. I'm attaching the Open Path logo and the introduction to the book.
Main themes include navigating today’s culture, understanding and using our spiritual gifts, and experiencing joy in community.

```html
<!DOCTYPE html>
<html lang="en">
<head>
<meta charset="utf-8">
<title>Walking Steady Onward — Book Cover</title>
<link rel="stylesheet" href="https://fonts.googleapis.com/css2?family=Montserrat:wght@300;400;500;600;700;800;900&display=swap">
<style>
  :root {
    --page: #ffffff;
    --cream: #e4e3d8;
    --navy: #03527a;
    --navy-ink: #0d5173;
    --gold-band: #c99a2c;
    --ink: #1f2a30;
    --white: #ffffff;
    --photo-grey: #a3a19c;
    --rule: #2f5563;
  }
  * { margin: 0; padding: 0; box-sizing: border-box; }
  html, body { width: 1200px; height: 900px; overflow: hidden; background: var(--page); }
  body { font-family: "Montserrat", sans-serif; position: relative; }

  .cover { position: absolute; left: 64px; top: 64px; width: 1072px; height: 771px; }

  /* Back cover */
  .back { position: absolute; left: 0; top: 0; width: 507px; height: 771px; background: var(--cream); }
  .back-title { position: absolute; left: 160px; top: 42px; width: 198px; height: 104px; }
  .body-copy {
    font-size: 10.6px; line-height: 14.3px; font-weight: 400; color: var(--ink);
    letter-spacing: -0.35px; text-align: justify; hyphens: auto; -webkit-hyphens: auto;
  }
  .back-blurb { position: absolute; left: 42px; top: 157px; width: 432px; }
  .back-blurb p + p { margin-top: 7px; }
  .author-rule {
    position: absolute; left: 26px; top: 374px; width: 459px; height: 28px;
    display: flex; align-items: center; gap: 12px;
  }
  .author-rule .rule-line { flex: 1; height: 1px; background: var(--rule); }
  .author-rule .rule-name { font-size: 22px; font-weight: 500; color: #111; line-height: 28px; white-space: nowrap; }
  .author-photo { position: absolute; left: 26px; top: 422px; width: 136px; height: 153px; background: var(--photo-grey); }
  .author-bio { position: absolute; left: 181px; top: 419px; width: 283px; }
  .barcode-area { position: absolute; left: 291px; top: 589px; width: 190px; height: 109px; border: 1px solid #8d8c86; }
  .publisher {
    position: absolute; left: 44px; top: 654px; width: 100px; text-align: center;
    font-size: 13px; font-weight: 700; color: #111; letter-spacing: 0.3px;
  }
  .publisher .dot { display: block; width: 10px; height: 10px; border-radius: 50%; background: #111; margin: 0 auto 8px; }

  /* Front cover */
  .front { position: absolute; left: 507px; top: 0; width: 565px; height: 771px; background: var(--navy); }
  .front-title { position: absolute; left: 90px; top: 40px; width: 432px; height: 228px; }
  .subtitle {
    position: absolute; left: 60px; right: 0; top: 306px; text-align: center;
    color: var(--white); font-size: 18px; font-weight: 500; letter-spacing: 0.6px; white-space: nowrap;
  }
  .band { position: absolute; left: 0; width: 565px; height: 5px; background: var(--gold-band); }
  .band.top { top: 357px; }
  .band.bottom { top: 684px; }
  .scene {
    position: absolute; left: 0; top: 362px; width: 565px; height: 322px;
    background: linear-gradient(180deg, #c9d3cf 0%, #b8b49a 35%, #6d8a3c 60%, #4a5e2a 80%, #7b6a54 100%);
  }
  .front-author {
    position: absolute; left: 0; right: 0; top: 704px; text-align: center;
    color: var(--white); font-size: 36px; line-height: 46px; font-weight: 500; letter-spacing: 0.4px;
  }
  .spine-title, .spine-author {
    position: absolute; left: 29px; writing-mode: vertical-rl; color: var(--white); white-space: nowrap;
  }
  .spine-title { top: 30px; font-size: 13.5px; font-weight: 800; letter-spacing: 3.1px; }
  .spine-author { top: 384px; font-size: 13px; font-weight: 500; }
</style>
</head>
<body>
<div class="cover">
  <section class="back">
    <svg class="back-title" viewBox="0 0 198 104" aria-label="Walking Steady Onward">
      <text x="99" y="29" text-anchor="middle" textLength="194" lengthAdjust="spacingAndGlyphs" font-family="Montserrat, sans-serif" font-weight="900" font-size="36" fill="#0d5173">WALKING</text>
      <text x="99" y="68" text-anchor="middle" textLength="194" lengthAdjust="spacingAndGlyphs" font-family="Montserrat, sans-serif" font-weight="900" font-size="48" fill="#0d5173">STEADY</text>
      <text x="99" y="102" text-anchor="middle" textLength="194" lengthAdjust="spacingAndGlyphs" font-family="Montserrat, sans-serif" font-weight="900" font-size="36" fill="#0d5173">ONWARD</text>
    </svg>

    <div class="back-blurb body-copy">
      <p>Lorem ipsum dolor sit amet, consectetuer adipiscing elit, sed diam nonummy nibh euismod tincidunt ut laoreet dolore magna aliquam erat volutpat. Ut wisi enim ad minim veniam, quis nostrud exerci tation ullamcorper suscipit lobortis nisl ut aliquip ex ea commodo consequat. Duis autem vel eum iriure dolor in hendrerit in vulputate velit esse molestie consequat, vel illum dolore eu feugiat nulla facilisis at vero eros et accumsan et iusto odio dignissim qui Lorem ipsum dolor sit amet, consectetuer adipiscing elit, sed diam nonummy nibh euismod tincidunt ut laoreet dolore magna aliquam erat volutpat. Ut wisi enim ad minim veniam, quis nostrud exerci tation ullamcorper suscipit lobortis nisl ut aliquip ex ea commodo consequat. Duis autem vel eum iriure dolor in hendrerit in vulputate velit esse molestie consequat, vel illum dolore eu feugiat nulla facilisis at vero eros et accumsan et iusto odio dignissim qui</p>
      <p>Lorem ipsum dolor sit amet, consectetuer adipiscing elit, sed diam nonummy nibh euismod tincidunt ut laoreet dolore magna aliquam erat volutpat. Ut wisi</p>
    </div>

    <div class="author-rule">
      <span class="rule-line"></span>
      <span class="rule-name">Dr. Martin Hale</span>
      <span class="rule-line"></span>
    </div>

    <div class="author-photo" role="img" aria-label="Author portrait placeholder"></div>
    <div class="author-bio body-copy">Lorem ipsum dolor sit amet, consectetuer adipiscing elit, sed diam nonummy nibh euismod tincidunt ut laoreet dolore magna aliquam erat volutpat. Ut wisi enim ad minim veniam, quis nostrud exerci tation ullamcorper suscipit lobortis nisl ut aliquip ex ea commodo consequat. Duis autem vel eum iriure dolor in hendrerit in vulputate velit esse molestie consequat, vel illum dolore eu feugiat nulla facilisis at vero eros et accumsan et iusto odio dignissim qui Lorem ipsum dolor sit amet, consectetuer adipiscing elit, sed diam nonummy nibh</div>

    <div class="barcode-area"></div>

    <div class="publisher"><span class="dot"></span>Open Path</div>
  </section>

  <section class="front">
    <svg class="front-title" viewBox="0 0 432 228" aria-label="Walking Steady Onward">
      <defs>
        <linearGradient id="gold" x1="0" y1="0" x2="0" y2="1">
          <stop offset="0" stop-color="#f0cc45"/>
          <stop offset="1" stop-color="#9d6f22"/>
        </linearGradient>
      </defs>
      <text x="216" y="63" text-anchor="middle" textLength="430" lengthAdjust="spacingAndGlyphs" font-family="Montserrat, sans-serif" font-weight="900" font-size="80" fill="url(#gold)">WALKING</text>
      <text x="216" y="155" text-anchor="middle" textLength="430" lengthAdjust="spacingAndGlyphs" font-family="Montserrat, sans-serif" font-weight="900" font-size="104" fill="url(#gold)">STEADY</text>
      <text x="216" y="226" text-anchor="middle" textLength="430" lengthAdjust="spacingAndGlyphs" font-family="Montserrat, sans-serif" font-weight="900" font-size="76" fill="url(#gold)">ONWARD</text>
    </svg>

    <div class="subtitle">SHAPED AS AN OPEN PATH FOLLOWER</div>

    <div class="band top"></div>
    <div class="scene" role="img" aria-label="Sunlit landscape with a winding stone path through grass and lavender, trees and distant mountains"></div>
    <div class="band bottom"></div>

    <div class="spine-title">WALKING STEADY ONWARD</div>
    <div class="spine-author">Dr. Martin Hale</div>

    <div class="front-author">Dr. Martin Hale</div>
  </section>
</div>
</body>
</html>
```